Event flyer for Sunday night Youth Group

Need a 4 x 6 or 5 x 7 flyer for a new youth group starting on April 14. The youth group is for students in middle school and high school so it needs to look fun and cool, but not childish. I prefer it not to include pictures of people unless it's so obscure you can't really see their faces. I've uploaded some pictures of flyers I like. I've also attached a couple versions of our logo to use on the flyer.
Information the flyer needs to include:
Youth Group
Sundays, 6-8pm (beginning April 14)
Location: Merriwick's - 4219 Hollowfern Ln S, Keizer, 97418
There will be dinner, games, friends, and a message.
Target Market(s)
Youth ages 13-18
Industry/Entity Type
Church
Colors
Designer to choose colors to be used in the design.
Look and feel

```html
<!DOCTYPE html>
<html lang="en">
<head>
<meta charset="utf-8">
<title>Youth Group – Wayfield Fellowship</title>
<link rel="stylesheet" href="https://fonts.googleapis.com/css2?family=Montserrat:ital,wght@0,300;0,400;0,500;0,600;0,800;1,700&display=swap">
<style>
  :root {
    --backdrop: #dcdcdc;
    --paper: #ffffff;
    --slate: #274452;
    --sage: #8a9882;
    --ink: #0d0d0d;
    --text: #1e1e1e;
    --faint: #e9ece8;
  }
  * { margin: 0; padding: 0; box-sizing: border-box; }
  html, body {
    width: 1200px; height: 1200px; overflow: hidden;
    background: var(--backdrop);
    font-family: "Montserrat", sans-serif;
  }
  .flyer {
    position: absolute; left: 237px; top: 56px;
    width: 725px; height: 1088px;
    background: var(--paper);
    overflow: hidden;
  }
  .brand { position: absolute; left: 0; top: 87px; width: 725px; }
  .brand-mark {
    position: absolute; left: 188px; top: 0;
    width: 80px; height: 80px; background: var(--slate);
  }
  .brand-name {
    position: absolute; left: 0; top: 150px; width: 456px;
    text-align: center; color: var(--slate);
    font-weight: 500; letter-spacing: 2px; line-height: 1.15;
  }
  .brand-name .line-one { display: block; font-size: 40px; }
  .brand-name .line-two { display: block; font-size: 22px; letter-spacing: 6px; }
  .dot-field {
    position: absolute; right: 10px; top: 70px;
    width: 70px; height: 186px; background: var(--faint);
  }
  .title {
    position: absolute; right: 46px; top: 400px;
    text-align: left; font-weight: 800; line-height: 1;
    font-size: 100px; letter-spacing: 1px;
  }
  .title .word-one { display: block; color: var(--ink); }
  .title .word-two { display: block; color: var(--slate); margin-top: 4px; }
  .corner-block {
    position: absolute; left: 0; top: 650px;
    width: 200px; height: 438px; background: var(--slate);
  }
  .corner-block svg { position: absolute; left: 81px; top: 380px; }
  .wave-field {
    position: absolute; right: 0; width: 60px; height: 38px; background: var(--faint);
  }
  .wave-field.upper { top: 630px; }
  .wave-field.lower { top: 970px; }
  .details {
    position: absolute; right: 46px; text-align: right; color: var(--text);
  }
  .schedule { top: 688px; }
  .schedule .days { font-size: 31px; font-weight: 600; color: var(--ink); }
  .schedule .start { font-size: 25px; font-weight: 400; margin-top: 4px; }
  .location { top: 842px; font-size: 23px; font-weight: 400; line-height: 1.45; }
  .offer {
    top: 960px; font-size: 24px; font-weight: 700; font-style: italic;
    line-height: 1.35; color: var(--ink);
  }
</style>
</head>
<body>
  <main class="flyer">
    <header class="brand">
      <div class="brand-mark"></div>
      <p class="brand-name"><span class="line-one">WAYFIELD</span><span class="line-two">FELLOWSHIP</span></p>
    </header>

    <div class="dot-field" role="img" aria-label="Grid of small slate dots"></div>

    <h1 class="title"><span class="word-one">YOUTH</span><span class="word-two">GROUP</span></h1>

    <div class="corner-block">
      <svg width="110" height="24" viewBox="0 0 110 24" aria-hidden="true">
        <polygon points="0,2 16,12 0,22" fill="#fff"/>
        <polygon points="30,2 46,12 30,22" fill="#fff"/>
        <polygon points="60,2 76,12 60,22" fill="#fff"/>
        <polygon points="90,2 106,12 90,22" fill="#fff"/>
      </svg>
    </div>

    <div class="wave-field upper" role="img" aria-label="Small wavy line accent"></div>
    <div class="wave-field lower" role="img" aria-label="Small wavy line accent"></div>

    <section class="details schedule">
      <p class="days">Sundays, 6-8pm</p>
      <p class="start">(beginning April 14)</p>
    </section>

    <address class="details location" style="font-style: normal;">
      Merriwick's - 4219 Hollowfern<br>
      Ln S, Keizer, 97418
    </address>

    <p class="details offer">There will be dinner, games,<br>friends, and a message.</p>
  </main>
</body>
</html>
```